Label design for outdoor terrace cleaner

We are Talmer Patio Living and searching for a modern, clean but colorful and exciting label packaging design. Our product is Freshstep Exterior and is a weedage and terrace cleaner. It is a consumer product for webshops and retail shops, which should stand out by design and colors. We also would like it to be very visibly appealing with a photo.

Label size: 240 mm x 176 mm

Logo: TALMER (Please adjust to any color you want)
Slogan: PATIO LIVING (as part of the logo)

Label text is dutch, if you need any help with that, please ask.
Updates

Low design quality

Target Market(s)

Outdoor cleaning, retail market, handy shops, consumer retail market

Industry/Entity Type

Cleaning Product

Colors

Designer to choose colors to be used in the design.

Requirements
Must have
• Original ideas, marketing thoughts, some extra brainstorming for an outstanding and original result including texts, that will have consumers see our product and want to buy it. Smart use of words, photos and colors.
Nice to have
• Bright and visibly appealing colors (should include green, but nothing standard) and photo
Should not have
• Standard, dull appearance

```html
<!DOCTYPE html>
<html lang="nl">
<head>
<meta charset="utf-8">
<title>Talmer Patio Living – Freshstep Exterior label</title>
<link rel="stylesheet" href="https://fonts.googleapis.com/css2?family=Questrial&family=Poiret+One&display=swap">
<style>
  :root {
    --page: #ffffff;
    --orange: #e4712d;
    --sky-top: #6fa3cf;
    --sky-low: #b9d3e6;
    --facade: #e9e2d8;
    --garden: #8aa35a;
    --paving: #cfc8bd;
    --blossom: #d9a7b0;
    --claim-area: #5f7424;
    --panel: rgba(255, 255, 255, 0.6);
    --ink: #1d1d1d;
    --white: #ffffff;
  }
  * { margin: 0; padding: 0; box-sizing: border-box; }
  html, body { width: 1131px; height: 1200px; overflow: hidden; background: var(--page); }
  .canvas { position: relative; width: 1131px; height: 1200px; }

  .label {
    position: absolute; left: 20px; top: 180px;
    width: 1091px; height: 801px; overflow: hidden;
  }
  .label__photo {
    position: absolute; inset: 0;
    background:
      radial-gradient(ellipse 260px 120px at 150px 40px, var(--blossom), transparent 70%),
      radial-gradient(ellipse 260px 120px at 950px 60px, var(--blossom), transparent 70%),
      radial-gradient(ellipse 200px 120px at 1030px 720px, #c4506e, transparent 70%),
      linear-gradient(180deg, var(--sky-top) 0%, var(--sky-low) 22%, var(--facade) 38%, var(--facade) 60%, var(--garden) 72%, var(--paving) 88%, var(--paving) 100%);
  }

  .brand-panel {
    position: absolute; left: 27px; top: 84px; width: 494px; height: 146px;
    background: rgba(210, 228, 240, 0.6); border-radius: 10px;
    display: flex; align-items: center; justify-content: center;
  }
  .brand-name {
    font-family: "Questrial", sans-serif; font-size: 118px; line-height: 1;
    color: var(--orange); letter-spacing: 2px;
  }
  .brand-slogan {
    position: absolute; left: 188px; top: 252px;
    font-family: "Questrial", sans-serif; font-size: 27px; color: var(--ink); letter-spacing: 1px;
  }

  .claims-area {
    position: absolute; left: 144px; top: 436px; width: 290px; height: 196px;
    background: var(--claim-area); border-radius: 14px; opacity: 0.9;
  }
  .claims {
    position: absolute; left: 139px; top: 452px; width: 300px;
    list-style: none; text-align: center;
    font-family: "Poiret One", sans-serif; font-size: 17px; font-weight: 400; color: var(--white);
  }
  .claims li { height: 42.5px; line-height: 22px; }

  .swoosh { position: absolute; left: 0; top: 0; }
  .tagline {
    position: absolute; left: 27px; top: 740px;
    font-family: "Questrial", sans-serif; font-size: 14px; line-height: 20px; color: var(--white);
  }

  .info-panel {
    position: absolute; background: var(--panel); border-radius: 10px;
    font-family: "Questrial", sans-serif; font-size: 12.5px; line-height: 29px; color: var(--ink);
    padding: 4px 16px 0 8px; text-align: justify;
  }
  .info-panel--use { left: 572px; top: 94px; width: 492px; height: 276px; }
  .info-panel--notes { left: 577px; top: 456px; width: 487px; height: 263px; }
  .info-panel h2 { font-size: 12.5px; font-weight: normal; }
  .info-panel ul { list-style: none; }
  .info-panel li::before { content: "•  "; }

  .caption {
    position: absolute; top: 1022px;
    font-family: "Questrial", sans-serif; font-size: 28px; color: var(--ink);
    transform: translateX(-50%);
  }
  .caption--front { left: 271px; }
  .caption--back { left: 815px; }
</style>
</head>
<body>
<div class="canvas">
  <section class="label">
    <div class="label__photo" role="img" aria-label="Photo of a modern white villa with blossoming trees, landscaped garden and paved terrace under a blue sky"></div>

    <div class="brand-panel"><span class="brand-name">TALMER</span></div>
    <div class="brand-slogan">PATIO LIVING</div>

    <div class="claims-area" role="img" aria-label="Green leaf decoration behind the product claims"></div>
    <ul class="claims">
      <li>Zonder glyfosfaat</li>
      <li>Concentraat zonder giftige stoffen</li>
      <li>Resultaat binnen enkele uren</li>
      <li>Voor paden en terrassen</li>
    </ul>

    <svg class="swoosh" width="1091" height="801" viewBox="0 0 1091 801" aria-hidden="true">
      <path d="M0 638 C60 700 160 720 300 728 C450 736 560 730 630 801 L0 801 Z" fill="var(--orange)"/>
    </svg>
    <p class="tagline">Groen terras.<br>De must-have reiniger voor alle type terrassen, voor ieder huishouden.</p>

    <div class="info-panel info-panel--use">
      <h2>Gebruiksaanwijzing:</h2>
      <ul>
        <li>Verdun het tot een 25% oplossing (bijv. 1 liter Freshstep Exterior en 3 liter water).</li>
        <li>Besproei of begiet het terras met deze oplossing. 2 liter per 10 m2. (1 liter Freshstep Exterior is dus voldoende voor ca. 20 m2 terras).</li>
        <li>Niet toepassen in de volle zon en als er binnen enkele uren veel neerslag wordt verwacht.</li>
        <li>Eventueel na enkele dagen het los gekomen vuil van het terras vegen of spuiten.</li>
      </ul>
    </div>

    <div class="info-panel info-panel--notes">
      <h2>Notes:</h2>
      <ul>
        <li>Op zeer hardnekkige vervuiling kan het product eventueel onverdund worden toegepast.</li>
        <li>Freshstep Exterior tast bij toepassing conform de gebruiksaanwijzing gangbare buiten (natuur)steen, tegels en hout niet aan.</li>
        <li>Voorkom dat reinigingsproducten in contact komen met gewassen en/of direct in het oppervlaktewater terecht komen.</li>
        <li>Neem veiligheidsmaatregel in acht bij het werken met het onverdunde product.</li>
      </ul>
    </div>
  </section>

  <span class="caption caption--front">Front</span>
  <span class="caption caption--back">Back</span>
</div>
</body>
</html>
```